Business Card Design

We would like a colorful, engaging, welcoming business card, utilizing our picture of a local lighthouse. We are a Church. We would like the design to mostly feature the colour blue.
Thank you so much to all Designers who sent in submissions to us - it was really hard to make a decision, they were all of such high quality. We would not hesitate to recommend Sketch Harbor to other churches/ businesses.
Kestrel Beacon Fellowship
Industry/Entity Type
Business
Contact Information for Business Card
Kestrel Beacon Fellowship Inc, 17 Merrow Rd, TALLOWVALE WA 6412, Ph: (08) 9517 4063, E: beaconfellowship@quorvex.example, Facebook logo - Kestrel Beacon Fellowship Inc, Sunday Service 10am, "For God sent not his Son into the world to condemn the world; but that the world through Him might be saved." John 3:17.

```html
<!DOCTYPE html>
<html lang="en">
<head>
<meta charset="utf-8">
<title>Kestrel Beacon Fellowship Inc – Business Card</title>
<link rel="stylesheet" href="https://fonts.googleapis.com/css2?family=Open+Sans:wght@400;600;700&display=swap">
<style>
  :root {
    --backdrop: #4a4a4a;
    --navy: #262d86;
    --royal: #1f5fc0;
    --cyan: #1ea9e4;
    --white: #ffffff;
    --sky-top: #14235e;
    --sky-mid: #2e56a8;
    --hill: #2c3a2c;
  }
  * { margin: 0; padding: 0; box-sizing: border-box; }
  html, body {
    width: 1200px; height: 999px; overflow: hidden;
    background: var(--backdrop);
    font-family: "Open Sans", Arial, sans-serif;
  }
  .card {
    position: absolute; left: 75px; top: 200px;
    width: 1050px; height: 600px; overflow: hidden;
    background:
      radial-gradient(ellipse 520px 420px at 560px 330px, var(--cyan) 0%, var(--royal) 55%, var(--navy) 100%);
    box-shadow: 0 6px 18px rgba(0,0,0,0.45);
  }
  .card__art { position: absolute; left: 0; top: 0; width: 1050px; height: 600px; }
  .card__name {
    position: absolute; left: 636px; top: 86px;
    color: var(--white); font-weight: 700; font-size: 38px; line-height: 52px;
  }
  .contact {
    position: absolute; left: 524px; height: 44px;
    display: flex; align-items: center; color: var(--white);
  }
  .contact__icon { width: 44px; height: 44px; flex: none; }
  .contact__rule { width: 3px; height: 44px; background: var(--white); margin: 0 22px 0 16px; }
  .contact--address { top: 390px; font-size: 19px; }
  .contact--phone { top: 456px; font-size: 32px; }
  .contact--email { top: 522px; font-size: 20px; }
</style>
</head>
<body>
  <div class="card">
    <svg class="card__art" viewBox="0 0 1050 600">
      <defs>
        <linearGradient id="sceneTone" x1="0" y1="0" x2="0" y2="1">
          <stop offset="0" stop-color="var(--sky-top)"/>
          <stop offset="0.38" stop-color="var(--sky-mid)"/>
          <stop offset="0.5" stop-color="#3a4a5e"/>
          <stop offset="1" stop-color="var(--hill)"/>
        </linearGradient>
      </defs>
      <path role="img" aria-label="Photograph of a local lighthouse on a hilltop at dusk, with light beams across a blue sky and coastal shrubs in the foreground"
            d="M0,0 H592 C560,250 480,460 330,538 H0 Z" fill="url(#sceneTone)"/>
      <path d="M565,225 C550,350 480,470 390,530" fill="none" stroke="rgba(255,255,255,0.55)" stroke-width="3"/>
    </svg>

    <h1 class="card__name">Kestrel Beacon<br>Fellowship Inc,</h1>

    <div class="contact contact--address">
      <svg class="contact__icon" viewBox="0 0 44 44" aria-hidden="true">
        <g fill="none" stroke="#fff" stroke-width="2.4">
          <circle cx="22" cy="22" r="18"/>
          <ellipse cx="22" cy="22" rx="8" ry="18"/>
          <line x1="4" y1="22" x2="40" y2="22"/>
          <path d="M7,13 H37 M7,31 H37"/>
        </g>
      </svg>
      <span class="contact__rule"></span>
      <span>17 Merrow Rd, TALLOWVALE WA 6412,</span>
    </div>

    <div class="contact contact--phone">
      <svg class="contact__icon" viewBox="0 0 44 44" aria-hidden="true">
        <rect x="2" y="2" width="40" height="40" rx="7" fill="#fff"/>
        <path d="M15,10 l5,0 2,8 -4,3 c2,5 4,7 8,9 l3,-4 8,3 0,5 c-2,3 -5,4 -9,2 C18,33 12,27 10,18 c-1,-4 1,-7 5,-8 Z" fill="var(--royal)"/>
      </svg>
      <span class="contact__rule"></span>
      <span>(08) 9517 4063</span>
    </div>

    <div class="contact contact--email">
      <svg class="contact__icon" viewBox="0 0 44 44" aria-hidden="true">
        <path d="M4,18 L22,6 L40,18 V38 H4 Z" fill="#fff"/>
        <path d="M4,18 L22,30 L40,18" fill="none" stroke="var(--royal)" stroke-width="2.4"/>
        <path d="M18,16 h8 v4 h3 l-7,6 -7,-6 h3 Z" fill="var(--royal)"/>
      </svg>
      <span class="contact__rule"></span>
      <span>beaconfellowship@quorvex.example</span>
    </div>
  </div>
</body>
</html>
```